Hello , we need a 1 page A4 flyer. the flyer needs a heading and then 4 sub headings and catagoring. The words on the attached example are the same length as our text. we are open to a new modern look and the information can be in 1 or 2 coloums. we are an australian law firm and I have also attachd our logo. the bottom 1/4 of the page is a graphic you need to allow space for. we have blue as a corporate colour and do not have a font or style. please use the 5 headings and we will complete the words / text afterwards so we will need the final version to be a word document. for assistance see www.juristcove.com.au
Industry/Entity Type
Legal
Look and feel

```html
<!DOCTYPE html>
<html lang="en">
<head>
<meta charset="utf-8">
<title>JuristCove Flyer</title>
<link rel="stylesheet" href="https://fonts.googleapis.com/css2?family=Montserrat:wght@800&family=Nunito+Sans:wght@400;600;700&display=swap">
<style>
:root{
  --stage:#e9ebee;
  --paper:#ffffff;
  --sky:#0aa0e0;
  --brand:#1276c9;
  --deep:#1577cf;
  --ink:#2f2f33;
  --accent:#d6b400;
  --dot:#e4e6ea;
}
*{margin:0;padding:0;box-sizing:border-box}
html,body{width:1200px;height:2754px;overflow:hidden;background:var(--stage)}
.flyer{position:absolute;left:0;top:528px;width:1200px;height:1697px;background:var(--paper);overflow:hidden;font-family:"Nunito Sans",sans-serif;color:var(--ink)}
.office-photo{position:absolute;left:700px;top:381px;width:500px;height:836px;background:radial-gradient(ellipse at 60% 45%,#e3e6ea 0%,#f2f3f5 55%,rgba(255,255,255,0) 80%)}
.brand{position:absolute;left:94px;top:110px;display:flex;align-items:center;gap:22px}
.brand-square{width:74px;height:74px;background:var(--sky)}
.brand-name{font-family:"Nunito Sans",sans-serif;font-weight:600;font-size:64px;color:var(--brand);letter-spacing:-0.5px}
.intro{position:absolute;left:537px;top:0;width:663px;height:381px;background:linear-gradient(180deg,#0aa3e3 0%,#0b9bdc 100%);color:#fff}
.intro-title{position:absolute;left:52px;top:62px;font-family:"Montserrat",sans-serif;font-weight:800;font-size:66px;line-height:70px;letter-spacing:0.5px}
.intro-stroke{position:absolute;left:52px;top:220px}
.intro-text{position:absolute;left:55px;top:264px;width:580px;font-size:17px;line-height:19px}
.section{position:absolute;left:0;width:1200px}
.section-icon{position:absolute;left:47px;top:0;width:58px;height:58px;border:4px solid var(--brand);background:#fff;display:flex;align-items:center;justify-content:center}
.section-icon svg{display:block}
.section-title{position:absolute;left:146px;top:10px;font-size:28px;font-weight:700;letter-spacing:0.2px;white-space:nowrap;text-transform:uppercase}
.section-rule{position:absolute;left:105px;top:54px;width:1048px;height:3px;background:var(--brand)}
.section-body{position:absolute;left:144px;top:76px;width:850px;font-size:16px;line-height:19.5px}
.section-body p+p{margin-top:17px}
.section-body.tight p+p{margin-top:0}
.dots{position:absolute;right:15px;top:1172px;display:flex;gap:17px}
.dots span{width:16px;height:16px;border-radius:50%;background:var(--dot)}
.contact-band{position:absolute;left:0;top:1217px;width:1200px;height:58px;background:var(--sky)}
.contact-band svg{position:absolute;left:0;top:0}
.contact-link{position:absolute;top:12px;color:#fff;font-size:27px;font-weight:600;white-space:nowrap}
.contact-link.web{left:208px}
.contact-link.mail{left:630px}
.skyline{position:absolute;left:0;top:1275px;width:1200px;height:422px;background:linear-gradient(180deg,#1679d2 0%,#1474cb 60%,#0f66b8 100%)}
</style>
</head>
<body>
<main class="flyer">
  <div class="office-photo" role="img" aria-label="Faded photo of professionals working in an office"></div>

  <div class="brand">
    <div class="brand-square"></div>
    <div class="brand-name">JuristCove</div>
  </div>

  <header class="intro">
    <h1 class="intro-title">WHO IS<br>JURISTCOVE?</h1>
    <svg class="intro-stroke" width="560" height="14" viewBox="0 0 560 14"><path d="M0 7 Q10 1 40 2 L540 4 Q560 7 540 10 L40 12 Q10 13 0 7Z" fill="#fff"/></svg>
    <p class="intro-text">This is a statement header small paragraph. This is a statement header small paragraph. This is a statement header small paragraph. This is a statement header small paragraph.</p>
  </header>

  <section class="section" style="top:405px">
    <div class="section-icon"><svg width="38" height="38" viewBox="0 0 38 38"><rect width="38" height="38" fill="#bfe6f7"/><circle cx="14" cy="12" r="5" fill="var(--accent)"/><path d="M5 30 Q14 16 23 30Z" fill="var(--accent)"/><path d="M22 24 L29 18 L35 24 V31 H22Z" fill="var(--accent)"/></svg></div>
    <h2 class="section-title">Next generation legal and lender process services</h2>
    <div class="section-rule"></div>
    <div class="section-body">
      <p>Paragraph 1. Paragraph 1. Paragraph 1. Paragraph 1. Paragraph 1. Paragraph 1. Paragraph 1. Paragraph 1. Paragraph 1. Paragraph 1. Paragraph 1. Paragraph 1. Paragraph 1. Paragraph 1. Paragraph 1. Paragraph 1.</p>
      <p>Paragraph 2. Paragraph 2. Paragraph 2. Paragraph 2. Paragraph 2. Paragraph 2. Paragraph 2. Paragraph 2. Paragraph 2. Paragraph 2. Paragraph 2. Paragraph 2. Paragraph 2. Paragraph 2. Paragraph 2. Paragraph 2. Paragraph 2. Paragraph 2. Paragraph 2.</p>
    </div>
  </section>

  <section class="section" style="top:619px">
    <div class="section-icon"><svg width="38" height="38" viewBox="0 0 38 38"><rect width="38" height="38" fill="#bfe6f7"/><circle cx="19" cy="9" r="5" fill="var(--accent)"/><path d="M4 20 L12 26 H26 L34 20 V24 L26 32 H12 L4 24Z" fill="var(--accent)"/><rect x="15" y="16" width="8" height="8" fill="var(--accent)"/></svg></div>
    <h2 class="section-title">How you will benefit from us</h2>
    <div class="section-rule"></div>
    <div class="section-body">
      <p>Paragraph 1. Paragraph 1. Paragraph 1. Paragraph 1. Paragraph 1. Paragraph 1. Paragraph 1. Paragraph 1. Paragraph 1. Paragraph 1. Paragraph 1. Paragraph 1. Paragraph 1. Paragraph 1. Paragraph 1. Paragraph 1. Paragraph 1. Paragraph 1. Paragraph 1. Paragraph 1. Paragraph 1. Paragraph 1. Paragraph 1. Paragraph 1. Paragraph 1. Paragraph 1. Paragraph 1. Paragraph 1. Paragraph 1. Paragraph 1. Paragraph 1. Paragraph 1. Paragraph 1. Paragraph 1.</p>
    </div>
  </section>

  <section class="section" style="top:818px">
    <div class="section-icon"><svg width="38" height="38" viewBox="0 0 38 38"><rect width="38" height="38" fill="#bfe6f7"/><circle cx="19" cy="19" r="13" fill="var(--accent)"/><path d="M12 19 L17 24 L26 14" stroke="#fff" stroke-width="3" fill="none"/></svg></div>
    <h2 class="section-title">We understand the importance of the work we do for you</h2>
    <div class="section-rule"></div>
    <div class="section-body">
      <p>Paragraph 1. Paragraph 1. Paragraph 1. Paragraph 1. Paragraph 1. Paragraph 1. Paragraph 1. Paragraph 1. Paragraph 1. Paragraph 1. Paragraph 1. Paragraph 1. Paragraph 1. Paragraph 1. Paragraph 1. Paragraph 1. Paragraph 1. Paragraph 1.</p>
      <p>Paragraph 2. Paragraph 2. Paragraph 2. Paragraph 2. Paragraph 2. Paragraph 2. Paragraph 2. Paragraph 2. Paragraph 2. Paragraph 2. Paragraph 2. Paragraph 2.</p>
    </div>
  </section>

  <section class="section" style="top:1039px">
    <div class="section-icon"><svg width="38" height="38" viewBox="0 0 38 38"><rect width="38" height="38" fill="#bfe6f7"/><path d="M9 5 H24 L31 12 V33 H9Z" fill="var(--accent)"/><circle cx="20" cy="21" r="6" fill="#fff"/></svg></div>
    <h2 class="section-title">Results, not just promises</h2>
    <div class="section-rule"></div>
    <div class="section-body tight">
      <p>Paragraph 1. Paragraph 1. Paragraph 1. Paragraph 1. Paragraph 1. Paragraph 1. Paragraph 1. Paragraph 1. Paragraph 1. Paragraph 1. Paragraph 1</p>
      <p>Paragraph 2. Paragraph 2. Paragraph 2. Paragraph 2. Paragraph 2. Paragraph 2. Paragraph 2. Paragraph 2.</p>
    </div>
  </section>

  <div class="dots"><span></span><span></span><span></span><span></span><span></span><span></span></div>

  <footer class="contact-band">
    <svg width="1200" height="58" viewBox="0 0 1200 58">
      <polygon points="150,56 198,3 612,3 564,56" fill="var(--brand)" stroke="#fff" stroke-width="4"/>
      <polygon points="585,56 633,3 1063,3 1015,56" fill="var(--brand)" stroke="#fff" stroke-width="4"/>
    </svg>
    <span class="contact-link web">www.juristcove.com.au</span>
    <span class="contact-link mail">enquiries@juristcove.com.au</span>
  </footer>

  <div class="skyline" role="img" aria-label="Blue-tinted city skyline photo"></div>
</main>
</body>
</html>
```